Migration Lawyers

Company: Thornbury & Co Lawyers & Migration Agents

Name: Gavin Rusholt BEc, LLB
Address: Level 19, 71 Pelham Street
Sydney, NSW, Australia 2000

Ph: +61 2 9357 2164
M: 0438261504
E: gavin@permit-nomadra.org.au
W: www.permit-nomadra.org.au

Target Market(s)

Migration Clients

Industry/Entity Type

It Company

Font styles to use
Script

Requirements
Must have
• Logo
Should not have
• Please scale the format to the printing size attached

```html
<!DOCTYPE html>
<html lang="en">
<head>
<meta charset="utf-8">
<title>Thornbury &amp; Co — Business Card</title>
<link rel="stylesheet" href="https://fonts.googleapis.com/css2?family=Libre+Baskerville:wght@700&family=Dancing+Script:wght@700&family=Josefin+Sans:wght@400&display=swap">
<style>
  :root {
    --page-bg: #d9d6d2;
    --card-black: #050203;
    --card-red: #d01a22;
    --card-red-mid: #9a0e14;
    --card-red-deep: #5a0609;
    --card-red-dark: #2a0204;
    --brand-ink: #1a0a0b;
    --text-light: #f6e4e4;
    --text-soft: #efc9c9;
  }
  * { margin: 0; padding: 0; box-sizing: border-box; }
  html, body { width: 1200px; height: 871px; overflow: hidden; }
  body {
    background: var(--page-bg);
    display: flex;
    align-items: center;
    justify-content: center;
    gap: 40px;
  }
  .card {
    width: 520px;
    height: 318px;
    position: relative;
    overflow: hidden;
    box-shadow: 0 8px 24px rgba(0,0,0,0.25);
  }
  .card-front {
    background:
      radial-gradient(ellipse 75% 90% at 50% 46%, var(--card-red) 0%, var(--card-red-mid) 38%, var(--card-red-deep) 60%, var(--card-black) 95%);
  }
  .brand {
    position: absolute;
    left: 50%;
    top: 50%;
    transform: translate(-50%, -50%);
    display: flex;
    align-items: center;
    gap: 14px;
    white-space: nowrap;
  }
  .brand-dot {
    width: 56px;
    height: 56px;
    border-radius: 50%;
    border: 2px solid var(--brand-ink);
    flex: none;
  }
  .brand-name {
    font-family: "Libre Baskerville", serif;
    font-weight: 700;
    color: var(--brand-ink);
    line-height: 1.15;
  }
  .brand-name .firm { display: block; font-size: 26px; }
  .brand-name .tagline { display: block; font-size: 12.5px; }

  .card-back {
    background:
      radial-gradient(ellipse 70% 90% at 80% 15%, var(--card-red) 0%, var(--card-red-deep) 55%, var(--card-red-dark) 100%);
  }
  .back-accent {
    position: absolute;
    left: -60px;
    top: 30px;
    width: 260px;
    height: 260px;
    border-radius: 50%;
    border: 2px solid rgba(255,255,255,0.06);
    background: radial-gradient(circle at 60% 40%, rgba(255,60,60,0.08), rgba(0,0,0,0.12));
  }
  .holder {
    position: absolute;
    right: 24px;
    top: 60px;
    font-family: "Dancing Script", cursive;
    font-weight: 700;
    font-size: 24px;
    letter-spacing: 2px;
    color: var(--text-light);
    white-space: nowrap;
  }
  .address, .contacts {
    position: absolute;
    font-family: "Josefin Sans", sans-serif;
    font-size: 12.5px;
    letter-spacing: 1.8px;
    color: var(--text-soft);
    line-height: 1.55;
    white-space: nowrap;
  }
  .address { left: 250px; top: 118px; }
  .contacts { left: 218px; top: 188px; list-style: none; }
  .contacts li { display: flex; gap: 18px; }
  .contacts .label { width: 10px; color: var(--text-light); }
</style>
</head>
<body>
  <section class="card card-front" aria-label="Card front">
    <div class="brand">
      <span class="brand-dot"></span>
      <p class="brand-name">
        <span class="firm">Thornbury &amp; Co</span>
        <span class="tagline">Lawyers &amp; Migration Agents</span>
      </p>
    </div>
  </section>

  <section class="card card-back" aria-label="Card back">
    <div class="back-accent"></div>
    <h1 class="holder">Gavin Rusholt BEc, LLB</h1>
    <p class="address">Level 19, 71 Pelham Street<br>Australia, Sydney, NSW, 2000</p>
    <ul class="contacts">
      <li><span class="label">P</span><span>+61 2 9357 2164</span></li>
      <li><span class="label">M</span><span>0438261504</span></li>
      <li><span class="label">E</span><span>gavin@permit-nomadra.org.au</span></li>
      <li><span class="label">W</span><span>www.permit-nomadra.org.au</span></li>
    </ul>
  </section>
</body>
</html>
```